PREMIUM AGENCY High End Business Card - A+++ Designers Wanted

** DO NOT ATTEMPT TO CONTACT ME THROUGH SEARCHING ON ZINTREL OR EMAILING ME THROUGH MY WEBSITE **

I need a fresh, contemporary business card designed using the logo attached (BRONSALK)

I have attached the font for BRONSALK

It must have a premium look and feel. The business card size must be STANDARD size.

You can submit either/both VERTICAL or HORIZONTAL designs.

FRONT: It must have the following sample information on

Paul Ardley
Director Operations
Mobile +61 452 118 906
Email paulardley@bronsalk.com
www.bronsalk.com

The REAR of the business card must have the words

IMAGINE SHAPE ONWARD

as part of the design, in the same font (NEXA) attached.

The words do not need to be in capitals, or on the same line, please design this as you see it best working.

ADDITIONAL INFORMATION
======================

The BRONSALK logo must be on the front of the card

I want Ultraviolet printing on the final design, to enhance either the NAME of the person OR the BRONSALK logo OR the words on the back of the card.

Target Market(s)

Agency, Advertising Agency, Creative, Designers

Industry/Entity Type

Media

Contact Information for Business Card

Design Agency, Contemporary, Premium look and feel, High Quality

Font styles to use
Serif
Sans Serif
Other font styles liked:
• ATTACHED TO PROJECT

Requirements
Must have
• BLACK & WHITE as the primary design, and if you feel there can be a highlighted colour, then this can be used.
• The Logo ICON attached is blue, this colour must not be changed.
• I have attached the partner brand BRONSALK MEDIA incase you need to manipulate the original files.
• ** DO NOT ATTEMPT TO CONTACT ME THROUGH SEARCHING ON ZINTREL OR EMAILING ME THROUGH MY WEBSITE **
Nice to have
• Must be Premium. I have attached some sample designs, that I like that would be a good inspiration for where this can be taken.
• My favourite design is is the KESTRAVUE2-BUSINESSCARD-TEMPLATE
Should not have
• No funny or silly standard / off the shelf designs

```html
<!DOCTYPE html>
<html lang="en">
<head>
<meta charset="utf-8">
<title>Bronsalk Media – Business Card</title>
<link rel="stylesheet" href="https://fonts.googleapis.com/css2?family=Montserrat:wght@600&family=Nunito+Sans:wght@400;600&display=swap">
<style>
  :root {
    --backdrop: #e6e4e0;
    --card-white: #ffffff;
    --card-grey: #e4e5e7;
    --brand-blue: #2ba6e1;
    --brand-blue-light: #45b9ee;
    --ink: #2b2d31;
    --on-blue: #ffffff;
    --card-w: 540px;
    --card-h: 309px;
  }
  * { box-sizing: border-box; margin: 0; padding: 0; }
  html, body { width: 1200px; height: 843px; overflow: hidden; }
  body {
    background: var(--backdrop);
    font-family: "Nunito Sans", Arial, sans-serif;
    display: flex;
    align-items: center;
    justify-content: center;
    gap: 40px;
  }
  .card {
    position: relative;
    width: var(--card-w);
    height: var(--card-h);
    overflow: hidden;
    box-shadow: 0 10px 28px rgba(0,0,0,0.18);
    background: linear-gradient(160deg, var(--card-white) 45%, var(--card-grey) 100%);
  }

  /* Rear */
  .card-back {
    display: flex;
    flex-direction: column;
    align-items: center;
    justify-content: center;
    gap: 30px;
  }
  .logotype {
    display: flex;
    align-items: center;
    gap: 12px;
  }
  .logotype-mark {
    width: 20px; height: 20px;
    border-radius: 50%;
    background: var(--brand-blue);
  }
  .logotype-name {
    font-family: "Montserrat", Arial, sans-serif;
    font-weight: 600;
    font-size: 30px;
    letter-spacing: 2px;
    color: var(--ink);
  }
  .tagline {
    font-family: "Montserrat", Arial, sans-serif;
    font-weight: 600;
    font-size: 12px;
    letter-spacing: 4px;
    color: var(--brand-blue);
  }

  /* Front */
  .front-panel {
    position: absolute;
    inset: 0;
    width: 100%;
    height: 100%;
  }
  .holder {
    position: absolute;
    left: 30px; top: 28px;
    color: var(--on-blue);
  }
  .holder-name {
    font-family: "Montserrat", Arial, sans-serif;
    font-weight: 600;
    font-size: 16px;
    letter-spacing: 1px;
    text-transform: uppercase;
  }
  .holder-role { font-size: 13px; font-weight: 600; margin-top: 2px; }
  .contact-list {
    position: absolute;
    left: 30px; bottom: 36px;
    list-style: none;
    color: var(--on-blue);
    font-size: 13px;
  }
  .contact-item {
    display: flex; align-items: center; gap: 10px;
    line-height: 21px;
  }
  .contact-icon { width: 13px; height: 13px; flex: none; }
  .front-wordmark {
    position: absolute;
    right: 30px; bottom: 34px;
    font-family: "Montserrat", Arial, sans-serif;
    font-weight: 600;
    font-size: 30px;
    letter-spacing: 4px;
    color: var(--ink);
  }
</style>
</head>
<body>
  <section class="card card-back" aria-label="Card rear">
    <div class="logotype">
      <span class="logotype-mark"></span>
      <span class="logotype-name">BRONSALK MEDIA</span>
    </div>
    <p class="tagline">IMAGINE SHAPE ONWARD</p>
  </section>

  <section class="card card-front" aria-label="Card front">
    <svg class="front-panel" viewBox="0 0 540 309" preserveAspectRatio="none" aria-hidden="true">
      <defs>
        <linearGradient id="panel-blue" x1="0" y1="0" x2="1" y2="0.4">
          <stop offset="0" stop-color="#2ba6e1"/>
          <stop offset="0.45" stop-color="#45b9ee"/>
          <stop offset="1" stop-color="#2ba6e1"/>
        </linearGradient>
      </defs>
      <path d="M0 0 H540 V20 C470 40 450 120 420 170 C400 200 330 195 300 220 C280 240 285 280 290 309 H0 Z" fill="url(#panel-blue)"/>
    </svg>
    <div class="holder">
      <p class="holder-name">Paul Ardley</p>
      <p class="holder-role">Director Operations</p>
    </div>
    <ul class="contact-list">
      <li class="contact-item">
        <svg class="contact-icon" viewBox="0 0 14 14" aria-hidden="true"><rect x="3.5" y="0.5" width="7" height="13" rx="1.2" fill="none" stroke="#fff" stroke-width="1.2"/><circle cx="7" cy="11.2" r="0.8" fill="#fff"/></svg>
        <span>+61 452 118 906</span>
      </li>
      <li class="contact-item">
        <svg class="contact-icon" viewBox="0 0 14 14" aria-hidden="true"><rect x="0.6" y="2.6" width="12.8" height="8.8" fill="#fff"/><path d="M0.6 2.6 L7 7.6 L13.4 2.6" fill="none" stroke="#2ba6e1" stroke-width="1.1"/></svg>
        <span>paulardley@bronsalk.com</span>
      </li>
      <li class="contact-item">
        <svg class="contact-icon" viewBox="0 0 14 14" aria-hidden="true"><circle cx="7" cy="7" r="6.2" fill="none" stroke="#fff" stroke-width="1.2"/><ellipse cx="7" cy="7" rx="2.6" ry="6.2" fill="none" stroke="#fff" stroke-width="1"/><line x1="0.8" y1="7" x2="13.2" y2="7" stroke="#fff" stroke-width="1"/></svg>
        <span>www.bronsalk.com</span>
      </li>
    </ul>
    <p class="front-wordmark">BRONSALK</p>
  </section>
</body>
</html>
```